earthmoving and roadworks company looking for a fresh and updated logo to help us stand out

We are looking for a business card design for our earthmoving, demolition and road works company named Wandermere Plant. We cover a broad range of work so our business card needs to be flexible to suit all of the different services we provide. We have a few different bits of machinery including several water trucks for transporting water and spraying the roads, an excavator (digger) for earthmoving, a tipper truck that carries grain/soil and other items, a bobcat and two rollers. our business card needs to be simple but effective and bold. Our colour palette is yellow, black and white and I have attached a copy of our logo but please note our logo is only the 'Wandermere plant' bit with attached circle, the 'watercarts, rollers, cartage' below are not part of the logo. Please feel free to modify the logo to better suit the business card. The design must be easy to read and to the point. It should make us look reliable and professional.

Target Market(s)

Wide range of clients including government sectors and private individuals

Industry/Entity Type

Construction

Contact Information for Business Card

We need a business card that is bold and straight to the point but with easy to read information and an eye catching design. We are open to either a single sided or double sided design

Colors
fbee3d
fcf5b5
fbf289
fbed22

Requirements
Must have
• The business card must include
• our logo
• our contact details as listed below:
• Trevor Okafor
• Managing Director
• 02 6140 9375
• 0471 903 216
• wandermereplant@fernmail.example
Nice to have
• Nice to have a picture of machinery or part of machinery in the business card design. We would also like to incorporate our business activities which are: demolition, earthmoving, road works and cartage. It would also be highly desirable if it included a list of our machinery: Watercarts, Rollers, Excavator, Bobcat, Truck & Dog. we are open to the possibility of either single sided or double sided designs
Should not have
• should not have too many colours or detract from the main information. should not be too busy.

```html
<!DOCTYPE html>
<html lang="en">
<head>
<meta charset="utf-8">
<title>Wandermere Plant — Business Card</title>
<link rel="stylesheet" href="https://fonts.googleapis.com/css2?family=Open+Sans:wght@300;400;700&family=Roboto+Slab:wght@800&display=swap">
<style>
  :root {
    --ink: #0b0b0b;
    --paper: #ffffff;
    --paper-shade: #e9e9e9;
    --brand-yellow: #fbed22;
    --soft-yellow: #fbf289;
    --stripe-grey: #a9a9a9;
    --text-dark: #1c1c1c;
    --stage: #ececec;
  }
  * { box-sizing: border-box; margin: 0; padding: 0; }
  html, body { width: 1200px; height: 892px; overflow: hidden; background: var(--stage); }
  .sheet {
    width: 1200px; height: 892px;
    display: flex; flex-direction: column; align-items: center; justify-content: center; gap: 36px;
  }
  .card {
    position: relative; width: 700px; height: 400px; overflow: hidden;
    background: var(--paper);
    box-shadow: 0 6px 18px rgba(0,0,0,.18);
    font-family: "Open Sans", sans-serif;
  }
  .card-back { background: linear-gradient(135deg, var(--paper) 40%, var(--paper-shade)); }

  .front-bands { position: absolute; inset: 0; }

  .services { position: absolute; left: 34px; top: 78px; color: var(--paper); font-family: "Roboto Slab", serif; font-weight: 800; line-height: 1.05; white-space: nowrap; }
  .services-main { font-size: 44px; letter-spacing: 1px; }
  .services-sub { font-size: 25px; letter-spacing: 1px; margin-top: 6px; }
  .card-back .services { position: static; color: var(--ink); text-align: left; }
  .card-back .services-main { font-size: 50px; }
  .card-back .services-sub { font-size: 28px; }

  .brand { display: flex; align-items: center; gap: 10px; }
  .brand-dot { width: 30px; height: 30px; border-radius: 50%; background: var(--brand-yellow); flex: none; }
  .brand-name { font-family: "Open Sans", sans-serif; font-weight: 700; font-size: 22px; color: var(--paper); white-space: nowrap; }
  .card-front .brand { position: absolute; right: 28px; top: 36px; }
  .card-back .brand-name { color: var(--ink); font-size: 34px; }
  .card-back .brand-dot { width: 44px; height: 44px; }

  .person { position: absolute; left: 40px; bottom: 44px; color: var(--text-dark); }
  .person-name { font-weight: 300; font-size: 38px; line-height: 1.1; white-space: nowrap; }
  .person-role { font-weight: 400; font-size: 18px; }

  .divider { position: absolute; left: 330px; top: 262px; width: 2px; height: 104px; background: var(--text-dark); }

  .contacts { position: absolute; left: 348px; top: 262px; list-style: none; color: var(--text-dark); font-size: 16px; line-height: 1.9; white-space: nowrap; }
  .contacts li { display: flex; align-items: center; gap: 10px; }
  .contact-icon { width: 16px; height: 16px; flex: none; }

  .back-layout { position: absolute; inset: 0; display: flex; flex-direction: column; align-items: center; justify-content: center; gap: 22px; }
  .tagline { font-size: 22px; color: var(--text-dark); }
</style>
</head>
<body>
<main class="sheet">

  <section class="card card-front" aria-label="Business card front">
    <svg class="front-bands" viewBox="0 0 700 400" aria-hidden="true">
      <path fill="var(--stripe-grey)" d="M0 0H700V196C620 200 560 214 500 240C430 270 410 250 380 250C330 250 300 246 260 260C180 285 80 270 0 270Z"/>
      <path fill="var(--brand-yellow)" d="M0 0H700V170C610 176 560 190 505 215C440 245 400 236 360 220C310 200 280 236 240 246C170 262 80 256 0 256Z"/>
      <path fill="var(--ink)" d="M0 0H700V158C610 162 555 178 500 202C440 230 400 222 360 206C310 186 280 220 240 232C170 248 80 244 0 244Z"/>
    </svg>

    <div class="services">
      <div class="services-main">WATERCARTS</div>
      <div class="services-sub">ROLLERS • CARTAGE</div>
    </div>

    <div class="brand">
      <span class="brand-dot"></span>
      <span class="brand-name">Wandermere Plant</span>
    </div>

    <div class="person">
      <div class="person-name">Trevor Okafor</div>
      <div class="person-role">managing director</div>
    </div>

    <span class="divider"></span>

    <ul class="contacts">
      <li>
        <svg class="contact-icon" viewBox="0 0 16 16" aria-hidden="true"><rect width="16" height="16" rx="2" fill="var(--ink)"/><path d="M4 4l2 0 1 3-1.2 1a6 6 0 0 0 2.2 2.2L9 9l3 1v2a1 1 0 0 1-1 1A8 8 0 0 1 3 5a1 1 0 0 1 1-1z" fill="var(--paper)"/></svg>
        02 6140 9375
      </li>
      <li>
        <svg class="contact-icon" viewBox="0 0 16 16" aria-hidden="true"><rect width="16" height="16" rx="2" fill="var(--ink)"/><rect x="5" y="3" width="6" height="10" rx="1" fill="var(--paper)"/><rect x="6" y="4.5" width="4" height="6" fill="var(--ink)"/></svg>
        0471 903 216
      </li>
      <li>
        <svg class="contact-icon" viewBox="0 0 16 16" aria-hidden="true"><rect width="16" height="16" rx="2" fill="var(--ink)"/><rect x="3" y="4.5" width="10" height="7" fill="var(--paper)"/><path d="M3 4.5l5 4 5-4" stroke="var(--ink)" stroke-width="1" fill="none"/></svg>
        wandermereplant@fernmail.example
      </li>
    </ul>
  </section>

  <section class="card card-back" aria-label="Business card back">
    <div class="back-layout">
      <div class="brand">
        <span class="brand-dot"></span>
        <span class="brand-name">Wandermere Plant</span>
      </div>
      <div class="services">
        <div class="services-main">WATERCARTS</div>
        <div class="services-sub">ROLLERS • CARTAGE</div>
      </div>
      <p class="tagline">Earthmoving, demolition road works and cartage.</p>
    </div>
  </section>

</main>
</body>
</html>
```